DRIFTFRAME studio

Design to be modern with colours of logo, maybe orange background. Include name, position, phone/WhatsApp email/web. Specialises in long form TIMELAPSE

Contact Information for Business Card

Marcel Okoro, filmmaker,/photographer, phone/WhatsApp +971529386047, email - marcel@driftframestudio.com www.driftframestudio.com, instagram @driftframestudio

Font styles to use
Sans Serif

Requirements
Must have
• Fresh, bright, modern, original
Marcel Okoro - Filmmaker/Photographer
Phone/WhatsApp +971 529 38 6047
email - marcel@driftfarmestudio.com
Web - driftfarmestudio.com
PoBox 584319, Dubai, UAE
instagram - driftframestudio
Should not have
• solid black background

```html
<!DOCTYPE html>
<html lang="en">
<head>
<meta charset="UTF-8">
<title>Driftframe Studio — Business Card</title>
<link href="https://fonts.googleapis.com/css2?family=Montserrat:wght@800&family=Arimo:wght@400;700&display=swap" rel="stylesheet">
<style>
  :root {
    --brand-orange: #f07522;
    --ink: #111111;
    --paper: #ffffff;
    --backdrop: #dcdcdc;
    --muted-ring: rgba(255, 255, 255, 0.9);
  }
  * { box-sizing: border-box; margin: 0; padding: 0; }
  html, body {
    width: 1200px;
    height: 900px;
    overflow: hidden;
    background: var(--backdrop);
    font-family: "Arimo", Arial, sans-serif;
  }
  .stage {
    position: relative;
    width: 1200px;
    height: 900px;
  }
  .card {
    position: absolute;
    left: 330px;
    width: 540px;
    height: 300px;
    border-radius: 26px;
    overflow: hidden;
    box-shadow: 0 10px 24px rgba(0, 0, 0, 0.18);
  }
  /* Front side */
  .card--front {
    top: 110px;
    background: var(--brand-orange);
    display: flex;
    align-items: center;
    justify-content: center;
    gap: 18px;
  }
  .front-mark {
    width: 64px;
    height: 64px;
    border: 5px solid var(--muted-ring);
    border-radius: 50%;
  }
  .front-name {
    font-family: "Montserrat", Arial, sans-serif;
    font-weight: 800;
    font-size: 36px;
    line-height: 1;
    color: var(--paper);
    letter-spacing: 0.5px;
  }
  /* Back side */
  .card--back {
    top: 470px;
    background: var(--paper);
    padding: 38px 40px;
  }
  .back-brand {
    display: flex;
    align-items: center;
    gap: 14px;
  }
  .back-mark {
    width: 52px;
    height: 52px;
    border: 5px solid var(--brand-orange);
    border-radius: 50%;
  }
  .back-name {
    font-family: "Montserrat", Arial, sans-serif;
    font-weight: 800;
    font-size: 30px;
    line-height: 1;
    color: var(--brand-orange);
  }
  .person {
    margin-top: 28px;
  }
  .person-name {
    font-family: "Montserrat", Arial, sans-serif;
    font-weight: 800;
    font-size: 19px;
    color: var(--brand-orange);
    text-transform: uppercase;
    letter-spacing: 0.3px;
  }
  .person-role {
    font-size: 15px;
    color: var(--ink);
    margin-top: 2px;
  }
  .contacts {
    list-style: none;
    margin-top: 14px;
    display: grid;
    gap: 4px;
  }
  .contact {
    display: flex;
    align-items: center;
    gap: 10px;
    font-size: 14px;
    color: var(--ink);
  }
  .contact svg {
    width: 16px;
    height: 16px;
    flex: none;
  }
  .accent { color: var(--brand-orange); }
  .social {
    position: absolute;
    right: 34px;
    bottom: 98px;
    display: flex;
    align-items: center;
    gap: 8px;
    font-size: 14px;
    color: var(--ink);
  }
  .social-dot {
    width: 14px;
    height: 14px;
    border-radius: 50%;
    background: var(--brand-orange);
  }
</style>
</head>
<body>
<main class="stage">

  <section class="card card--front" aria-label="Business card front">
    <span class="front-mark"></span>
    <span class="front-name">DRIFTFRAME studio</span>
  </section>

  <section class="card card--back" aria-label="Business card back">
    <div class="back-brand">
      <span class="back-mark"></span>
      <span class="back-name">DRIFTFRAME studio</span>
    </div>

    <div class="person">
      <p class="person-name">Marcel Okoro</p>
      <p class="person-role">Filmmaker . Photographer</p>
    </div>

    <ul class="contacts">
      <li class="contact">
        <svg viewBox="0 0 24 24" aria-hidden="true"><path fill="none" stroke="#f07522" stroke-width="2.4" stroke-linecap="round" d="M6 3l4 4-2 3c1 2 4 5 6 6l3-2 4 4-3 3C10 21 3 14 3 6z"/></svg>
        <span>+971529386047</span>
      </li>
      <li class="contact">
        <svg viewBox="0 0 24 24" aria-hidden="true"><rect x="2" y="5" width="20" height="14" fill="#f07522"/><path d="M2 5l10 8 10-8" fill="none" stroke="#fff" stroke-width="2"/></svg>
        <span>marcel@driftframestudio.com</span>
      </li>
      <li class="contact">
        <svg viewBox="0 0 24 24" aria-hidden="true"><g fill="none" stroke="#f07522" stroke-width="2"><circle cx="12" cy="12" r="9"/><ellipse cx="12" cy="12" rx="4" ry="9"/><path d="M3 12h18M5 7h14M5 17h14"/></g></svg>
        <span>www.<span class="accent">driftframestudio</span>.com</span>
      </li>
      <li class="contact">
        <svg viewBox="0 0 24 24" aria-hidden="true"><path fill="#f07522" d="M12 2a7 7 0 0 0-7 7c0 5 7 13 7 13s7-8 7-13a7 7 0 0 0-7-7zm0 9.5A2.5 2.5 0 1 1 12 6.5a2.5 2.5 0 0 1 0 5z"/></svg>
        <span>PO Box 584319 , Dubai, UAE</span>
      </li>
    </ul>

    <div class="social">
      <span class="social-dot"></span>
      <span>@driftframestudio</span>
    </div>
  </section>

</main>
</body>
</html>
```